Electrician's Business needs web site for customers to get professional impression of business.

Have a logo, need a web page for customers to visit. Web page should make it easy for customers to approach /contact me, if possible a way for customers to leave their details so I can call them back.
A description/ list of services and advertise how my service is different and better than other electricians.
A gallery to upload photos to, to show completed works from past projects.
Updates

Target Market(s)

Domestic/residential home owner/renter/builder

Industry/Entity Type

Electrician

Coding

Coded - Design and coding required

Number of Pages Required

2 page

Font styles to use
Sans Serif

Colors
0255a3
ffffff

Requirements
Must have
• Appeal to home owner/renter, domestic market.
• Capture contact details of customer & advertise my contact details.
• List of services
Nice to have
• A photo gallery, so I can upload pictures of completed work.
Should not have
• Industrial/construction images.

```html
<!DOCTYPE html>
<html lang="en">
<head>
<meta charset="utf-8">
<title>VoltNest Electrical Services</title>
<link rel="stylesheet" href="https://fonts.googleapis.com/css2?family=Exo+2:wght@500;600;700&family=Lato:wght@400;700&display=swap">
<style>
:root{
  --blue:#0d4c94;
  --blue-deep:#0a3d7a;
  --orange:#f07f1a;
  --white:#ffffff;
  --ink:#333a44;
  --muted:#666c74;
  --line:#c9ccd0;
  --card:#f6f6f6;
  --footer:#1f242b;
  --footer-text:#c4c8cd;
}
*{box-sizing:border-box;margin:0;padding:0}
html,body{width:1200px;height:2242px;overflow:hidden;background:var(--white)}
body{position:relative;font-family:"Lato",sans-serif;color:var(--ink)}
.abs{position:absolute}
.heading{font-family:"Exo 2",sans-serif}

/* header */
.header{left:0;top:0;width:1200px;height:114px;background:var(--white)}
.brand-band{left:0;top:0;width:490px;height:114px}
.brand{left:98px;top:28px;display:flex;align-items:center;gap:12px}
.brand-dot{width:16px;height:16px;border-radius:50%;background:var(--orange)}
.brand-name{font-family:"Exo 2",sans-serif;font-weight:700;font-size:31px;color:var(--white);line-height:1}
.brand-sub{font-family:"Exo 2",sans-serif;font-weight:700;font-size:31px;color:var(--white)}
.contact-top{top:17px;display:flex;align-items:center;gap:10px;font-size:15px;color:var(--ink)}
.contact-icon{width:28px;height:28px;border-radius:50%;border:2px solid var(--orange);display:flex;align-items:center;justify-content:center}
.nav{top:64px;left:557px;display:flex;font-size:15.5px;color:var(--ink)}
.nav a{color:inherit;text-decoration:none}
.nav .sep{color:var(--ink);margin:0 30px}
.nav .active{color:var(--orange)}

/* hero */
.hero{left:0;top:114px;width:1200px;height:428px;background:linear-gradient(180deg,#1e2a44 0%,#2d3a56 45%,#5a5648 78%,#2b3524 100%)}
.hero-caption{left:97px;top:318px;width:560px;height:123px;background:rgba(20,24,34,.55);padding:10px 16px}
.hero-title{font-family:"Exo 2",sans-serif;font-weight:600;font-size:33px;color:var(--orange);line-height:1.1}
.hero-sub{font-family:"Exo 2",sans-serif;font-weight:600;font-size:20px;color:var(--white);line-height:1.6;margin-top:6px}
.hero-dots{left:573px;top:506px;display:flex;gap:5px}
.hero-dots span{width:11px;height:11px;border-radius:50%;background:var(--blue);border:2px solid var(--white)}
.hero-dots span.on{background:var(--orange)}

/* services */
.service{top:604px;width:262px;height:251px;background:var(--card);border:1px solid #e1e1e1;border-radius:3px;text-align:center;box-shadow:0 10px 10px -8px rgba(0,0,0,.25)}
.service.featured{background:#a9a9a9;border:3px solid #a9a9a9;outline:2px solid #fff;outline-offset:-9px}
.service-icon{position:absolute;left:78px;top:22px;width:105px;height:105px;border-radius:50%;background:var(--blue);border:3px solid var(--white);outline:2px solid var(--blue);display:flex;align-items:center;justify-content:center}
.service.featured .service-icon{background:#a9a9a9;outline-color:#d4d4d4;left:76px;top:20px}
.service-title{position:absolute;left:0;right:0;top:143px;font-family:"Exo 2",sans-serif;font-weight:500;font-size:16.5px;color:#222}
.service.featured .service-title,.service.featured .service-text{color:var(--white)}
.service-text{position:absolute;left:18px;right:18px;top:172px;font-size:11.5px;line-height:19px;color:#444}

/* about + quote */
.split{left:0;top:920px;width:1200px;height:366px}
.about-title{left:161px;top:950px;font-family:"Exo 2",sans-serif;font-weight:700;font-size:26px;color:var(--white)}
.about-title span,.gallery-title span,.footer-title span{color:var(--orange)}
.divider{height:1px;background:rgba(255,255,255,.35)}
.divider-mark{width:8px;height:8px;border-radius:50%}
.about-text{left:161px;top:1024px;width:435px;font-size:11.8px;line-height:24px;color:var(--white)}
.btn{display:flex;align-items:center;font-family:"Exo 2",sans-serif;font-weight:600;color:var(--white);border-radius:4px;overflow:hidden}
.btn-label{height:100%;display:flex;align-items:center;padding-left:15px}
.btn-tab{height:100%;background:#5d6166}
.read-more{left:161px;top:1191px;width:150px;height:40px;font-size:14px}
.read-more .btn-label{background:var(--orange);width:105px}
.read-more .btn-tab{width:45px}
.quote-title{left:726px;top:966px;font-family:"Exo 2",sans-serif;font-weight:600;font-size:21px;color:var(--white)}
.field{background:var(--white);border-radius:3px;font-size:10px;color:#999;padding:9px 11px}
.submit{left:726px;top:1210px;width:127px;height:40px;font-size:14px}
.submit .btn-label{background:var(--blue);width:85px}
.submit .btn-tab{width:42px}

/* gallery */
.gallery-title{left:0;width:1200px;top:1334px;text-align:center;font-family:"Exo 2",sans-serif;font-weight:700;font-size:24px;color:var(--blue)}
.gallery-line{left:161px;top:1387px;width:877px;height:1px;background:var(--line)}
.gallery-mark{left:595px;top:1382px;width:10px;height:10px;border-radius:50%;background:#9a9ea3;border:2px solid var(--white)}
.photo{background:#eeeeee;border:1px solid #dcdcdc;padding:10px}
.photo div{width:100%;height:100%}

/* footer */
.footer{left:0;top:1969px;width:1200px;height:227px;background:var(--footer)}
.footer-title{top:1995px;font-family:"Exo 2",sans-serif;font-weight:700;font-size:15.5px;color:var(--white)}
.footer-rule{top:2021px;height:1px;background:#4a4f57}
.quick-links{left:161px;top:2030px;list-style:none;font-size:11.5px;line-height:27px;color:var(--footer-text)}
.quick-links li::before{content:"• ";color:var(--footer-text)}
.quick-links li.active,.quick-links li.active::before{color:var(--orange)}
.contact-info{left:312px;top:2030px;width:200px;font-size:11.5px;color:var(--footer-text);line-height:16px}
.contact-info strong{display:block;color:var(--white);font-size:13px;margin-bottom:2px}
.contact-row{display:flex;align-items:center;gap:10px;margin-top:12px}
.map{left:548px;top:2031px;width:194px;height:128px;border:3px solid var(--white);background:linear-gradient(135deg,#dfe7d2 0%,#e9e3d3 50%,#bcd3e6 100%)}
.footer-brand{left:790px;top:1954px;width:248px;height:242px;background:var(--orange)}
.footer-brand .brand-line{position:absolute;left:0;right:0;top:93px;display:flex;justify-content:center;align-items:center;gap:8px}
.footer-brand .brand-name{font-size:24px}
.footer-brand .brand-dot{width:12px;height:12px;background:var(--white)}
.follow{position:absolute;left:0;right:0;top:170px;text-align:center;font-size:11.5px;color:var(--white)}
.social{position:absolute;left:0;right:0;top:194px;display:flex;justify-content:center;gap:9px}
.social span{width:22px;height:22px;background:#1f242b}
.copyright-bar{left:0;top:2196px;width:1200px;height:46px;background:var(--orange)}
.copyright{left:161px;top:2209px;font-size:11.5px;color:var(--white)}
</style>
</head>
<body>

<!-- header -->
<header class="abs header">
  <svg class="abs brand-band" viewBox="0 0 490 114" aria-hidden="true">
    <polygon points="0,0 448,0 410,114 0,114" fill="var(--blue)"/>
    <polygon points="448,0 482,0 444,114 410,114" fill="var(--orange)"/>
  </svg>
  <div class="abs brand">
    <span class="brand-name">VoltNest</span>
    <span class="brand-dot"></span>
  </div>
  <div class="abs" style="left:98px;top:68px;font-family:'Exo 2',sans-serif;font-weight:700;font-size:17px;color:var(--white)">Electrical Services</div>

  <div class="abs contact-top" style="left:720px">
    <span class="contact-icon"><svg width="13" height="13" viewBox="0 0 24 24"><path fill="var(--orange)" d="M6.6 10.8a15.1 15.1 0 0 0 6.6 6.6l2.2-2.2c.3-.3.7-.4 1-.2 1.1.4 2.3.6 3.6.6.6 0 1 .4 1 1V20c0 .6-.4 1-1 1A17 17 0 0 1 3 4c0-.6.4-1 1-1h3.5c.6 0 1 .4 1 1 0 1.3.2 2.5.6 3.6.1.3 0 .7-.2 1z"/></svg></span>
    <span>0400 123 456</span>
  </div>
  <div class="abs contact-top" style="left:873px">
    <span class="contact-icon"><svg width="13" height="11" viewBox="0 0 24 18"><rect x="1" y="1" width="22" height="16" rx="2" fill="var(--orange)"/><path d="M2 2l10 8 10-8" stroke="#fff" stroke-width="2" fill="none"/></svg></span>
    <span>info@voltnest.com.au</span>
  </div>

  <nav class="abs nav">
    <a class="active" href="#">Home</a><span class="sep">|</span>
    <a href="#">About Us</a><span class="sep">|</span>
    <a href="#">Services</a><span class="sep">|</span>
    <a href="#">Gallery</a><span class="sep">|</span>
    <a href="#">Contact Us</a>
  </nav>
</header>

<!-- hero -->
<section class="abs hero" role="img" aria-label="Modern two-storey home lit up at dusk"></section>
<div class="abs hero-caption">
  <h1 class="hero-title">We Are Team Of Electricians</h1>
  <p class="hero-sub">By Profession -&nbsp; Lighting Specialist, License<br>Electrician, Recess Lighting Experts</p>
</div>
<div class="abs hero-dots"><span></span><span class="on"></span><span class="on"></span><span></span></div>

<!-- services -->
<article class="abs service" style="left:176px">
  <div class="service-icon">
    <svg width="44" height="40" viewBox="0 0 44 40"><path d="M22 3L3 19h5v18h28V19h5z" fill="#fff"/><rect x="15" y="22" width="6" height="6" fill="var(--blue)"/><rect x="23" y="22" width="6" height="6" fill="var(--blue)"/><rect x="15" y="30" width="6" height="6" fill="var(--blue)"/><rect x="23" y="30" width="6" height="6" fill="var(--blue)"/></svg>
  </div>
  <h2 class="service-title">DOMESTIC ELECTRICIAN</h2>
  <p class="service-text">Lorem ipsum dolor sit amet, consectetuer adipiscing elit,sed consectetuer adipiscing elit,sed diam nonummy.</p>
</article>
<article class="abs service featured" style="left:469px">
  <div class="service-icon">
    <svg width="40" height="44" viewBox="0 0 40 44"><rect x="6" y="4" width="28" height="38" fill="#fff"/><g fill="#a9a9a9"><rect x="11" y="9" width="5" height="5"/><rect x="18" y="9" width="5" height="5"/><rect x="25" y="9" width="5" height="5"/><rect x="11" y="17" width="5" height="5"/><rect x="18" y="17" width="5" height="5"/><rect x="25" y="17" width="5" height="5"/><rect x="11" y="25" width="5" height="5"/><rect x="25" y="25" width="5" height="5"/><rect x="17" y="32" width="7" height="10"/></g></svg>
  </div>
  <h2 class="service-title">COMMERCIAL ELECTRICIAN</h2>
  <p class="service-text">Lorem ipsum dolor sit amet, consectetuer adipiscing elit,sed consectetuer adipiscing elit,sed diam nonummy.</p>
</article>
<article class="abs service" style="left:762px">
  <div class="service-icon" role="img" aria-label="Electrician in hard hat"></div>
  <h2 class="service-title">STRATA ELECTRICIAN</h2>
  <p class="service-text">Lorem ipsum dolor sit amet, consectetuer adipiscing elit,sed consectetuer adipiscing elit,sed diam nonummy.</p>
</article>

<!-- about + quote -->
<svg class="abs split" viewBox="0 0 1200 366" aria-hidden="true">
  <polygon points="0,0 708,0 727,18 589,366 0,348" fill="var(--blue)"/>
  <polygon points="708,18 1200,18 1200,366 575,366" fill="var(--orange)"/>
  <polygon points="562,348 575,348 580,362" fill="var(--blue-deep)"/>
</svg>

<h2 class="abs about-title">ABOUT <span>US</span></h2>
<div class="abs divider" style="left:178px;top:1001px;width:416px"></div>
<div class="abs divider-mark" style="left:161px;top:997px;background:rgba(255,255,255,.45)"></div>
<p class="abs about-text">Lorem ipsum dolor sit amet, consectetuer adipiscing elit, sed diam nonummy nibh euismod tincidunt ut laoreet dolore magna aliquam erat volutpat. Ut wisi enim ad minim veniam, quis nostrud exerci tation ullamcorper suscipit lobortis nisl ut aliquip ex ea commodo consequat. Duis autem vel eum iriure dolor in hendrerit in vulputate velit esse molestie consequat, vel illum dolore eu feugiat nulla facilisis at vero eros et accumsan et iusto odio dignissim qui blandit praesent.</p>
<div class="abs btn read-more"><span class="btn-label">READ MORE</span><span class="btn-tab"></span></div>

<h2 class="abs quote-title">Request a Free Quote/Call Back</h2>
<div class="abs divider" style="left:742px;top:1019px;width:296px"></div>
<div class="abs divider-mark" style="left:726px;top:1015px;background:rgba(255,255,255,.5)"></div>
<div class="abs field" style="left:726px;top:1043px;width:312px;height:30px">Full Name</div>
<div class="abs field" style="left:726px;top:1080px;width:146px;height:30px">Email</div>
<div class="abs field" style="left:880px;top:1080px;width:158px;height:30px">Email</div>
<div class="abs field" style="left:726px;top:1118px;width:312px;height:62px">Full Name</div>
<div class="abs btn submit"><span class="btn-label">SUBMIT</span><span class="btn-tab"></span></div>

<!-- gallery -->
<h2 class="abs gallery-title">PHOTO <span>GALLERY</span></h2>
<div class="abs gallery-line"></div>
<div class="abs gallery-mark"></div>

<div class="abs photo" style="left:161px;top:1424px;width:431px;height:234px"><div role="img" aria-label="Electrician testing a switchboard with a multimeter" style="background:linear-gradient(135deg,#4a6aa0,#9aa6b4 55%,#d7d9dc)"></div></div>
<div class="abs photo" style="left:604px;top:1424px;width:209px;height:297px"><div role="img" aria-label="Electrician working on a panel" style="background:linear-gradient(160deg,#c98a4a,#8f6a55 45%,#6f7f93)"></div></div>
<div class="abs photo" style="left:829px;top:1424px;width:208px;height:231px"><div role="img" aria-label="Electrician at a fuse board" style="background:linear-gradient(150deg,#d9c06a,#6e6f72 50%,#b7b9bc)"></div></div>
<div class="abs photo" style="left:161px;top:1673px;width:210px;height:227px"><div role="img" aria-label="Electrician pulling cables" style="background:linear-gradient(160deg,#3a63a8,#2d3e66 50%,#8a8d96)"></div></div>
<div class="abs photo" style="left:384px;top:1673px;width:208px;height:227px"><div role="img" aria-label="Electrician wiring a wall" style="background:linear-gradient(150deg,#e0c34f,#9ea3ab 45%,#3b5a8c)"></div></div>
<div class="abs photo" style="left:604px;top:1738px;width:209px;height:162px"><div role="img" aria-label="Team of electricians inspecting a panel" style="background:linear-gradient(140deg,#e4e4e4,#8fa0b4 50%,#5a6a7e)"></div></div>
<div class="abs photo" style="left:829px;top:1669px;width:208px;height:231px"><div role="img" aria-label="Close-up of a multimeter on a switchboard" style="background:linear-gradient(150deg,#c8ccd2,#33498a 55%,#d9b23e)"></div></div>

<!-- footer -->
<footer class="abs footer"></footer>

<h3 class="abs footer-title" style="left:163px">QUICK <span>LINKS</span></h3>
<div class="abs footer-rule" style="left:163px;width:98px"></div>
<ul class="abs quick-links">
  <li class="active">Home</li>
  <li>About Us</li>
  <li>Our Services</li>
  <li>Photo Gallery</li>
  <li>Contact Us</li>
</ul>

<h3 class="abs footer-title" style="left:312px">CONTACT <span>INFORMATION</span></h3>
<div class="abs footer-rule" style="left:312px;width:190px"></div>
<div class="abs contact-info">
  <strong>VoltNest Electrical Services</strong>
  Lorem ipsum dolor sitamet, conetuer adipiscing sed diam nonummy.
  <div class="contact-row"><svg width="11" height="11" viewBox="0 0 24 24"><path fill="var(--footer-text)" d="M6.6 10.8a15.1 15.1 0 0 0 6.6 6.6l2.2-2.2c.3-.3.7-.4 1-.2 1.1.4 2.3.6 3.6.6.6 0 1 .4 1 1V20c0 .6-.4 1-1 1A17 17 0 0 1 3 4c0-.6.4-1 1-1h3.5c.6 0 1 .4 1 1 0 1.3.2 2.5.6 3.6.1.3 0 .7-.2 1z"/></svg>0400 123 456</div>
  <div class="contact-row"><svg width="11" height="9" viewBox="0 0 24 18"><rect x="1" y="1" width="22" height="16" rx="2" fill="var(--footer-text)"/><path d="M2 2l10 8 10-8" stroke="#1f242b" stroke-width="2" fill="none"/></svg>info@voltnest.com.au</div>
  <div class="contact-row"><svg width="11" height="11" viewBox="0 0 24 24"><circle cx="12" cy="12" r="10" fill="none" stroke="var(--footer-text)" stroke-width="3"/><path d="M2 12h20M12 2c4 4 4 16 0 20M12 2c-4 4-4 16 0 20" stroke="var(--footer-text)" stroke-width="2" fill="none"/></svg>www.voltnest.com.au</div>
</div>

<h3 class="abs footer-title" style="left:548px">LOCATION <span>MAP</span></h3>
<div class="abs footer-rule" style="left:548px;width:194px"></div>
<div class="abs map" role="img" aria-label="Street map showing the business location"></div>

<div class="abs footer-brand">
  <div class="brand-line"><span class="brand-name">VoltNest</span><span class="brand-dot"></span></div>
  <p class="follow">Follow Us:</p>
  <div class="social" aria-label="Social links"><span></span><span></span><span></span><span></span></div>
</div>

<div class="abs copyright-bar"></div>
<p class="abs copyright">Copyright © 2016 VoltNest Electrical Services. All Rights Reserved</p>

</body>
</html>
```